We sell companies excess stock for them

We need a business card for a company based in New Zealand called 'StockHarbor'.

Check out our website to get an idea www.stockharbor.example

We help other businesses to;
- Sell Excess Stock
- Manage Product Returns
- Sell Company Assets

Our logo is attached for your reference
The font used is 'RifficFree-Bold'

Target Market(s)

Businesses

Industry/Entity Type

Business

Contact Information for Business Card

Name: Mark Pellow
Phone: 027 846 2093
email: markpellow@stockharbor.example
website: www.stockharbor.example

Font styles to use
Other font styles liked:
• Unsure

Colors
9bcb3b

Requirements
Must have
• coming soon
Nice to have
• coming soon
Should not have
• coming soon

```html
<!DOCTYPE html>
<html lang="en">
<head>
<meta charset="utf-8">
<title>StockHarbor Business Card</title>
<link href="https://fonts.googleapis.com/css2?family=Fredoka:wght@600&family=Open+Sans:wght@400;600&display=swap" rel="stylesheet">
<style>
  :root {
    --green: #8dc63f;
    --ink: #2b2826;
    --paper: #ffffff;
    --backdrop: #3b3b3d;
    --muted: #3a3a3a;
  }
  * { margin: 0; padding: 0; box-sizing: border-box; }
  html, body { width: 1200px; height: 900px; overflow: hidden; }
  body { background: var(--backdrop); position: relative; font-family: "Open Sans", Arial, sans-serif; }

  .card {
    position: absolute; left: 250px; width: 700px; height: 400px;
    background: var(--paper); border-radius: 26px; overflow: hidden;
    box-shadow: 0 10px 24px rgba(0,0,0,.35);
  }
  .card--front { top: 30px; }
  .card--back { top: 470px; }

  /* front */
  .holder { position: absolute; left: 60px; top: 52px; }
  .holder__name { font-family: "Fredoka", "Arial Rounded MT Bold", sans-serif; font-weight: 600; font-size: 34px; color: var(--ink); line-height: 1; }
  .holder__role { font-size: 15px; color: var(--green); margin-top: 2px; }
  .holder__rule { width: 80px; height: 3px; background: var(--green); margin-top: 12px; }

  .contacts { position: absolute; left: 60px; top: 160px; list-style: none; }
  .contacts li { display: flex; align-items: center; gap: 12px; font-size: 16px; color: var(--muted); height: 27px; }
  .contacts svg { width: 16px; height: 16px; flex: none; }

  .band { position: absolute; }
  .band--dark { left: 0; top: 258px; width: 318px; height: 34px; background: var(--ink); }
  .band--green { left: 350px; top: 318px; width: 350px; height: 34px; background: var(--green); }

  .brand { position: absolute; display: flex; align-items: center; gap: 14px; }
  .brand__mark { width: 54px; height: 54px; border-radius: 50%; background: var(--green); flex: none; }
  .brand__name { font-family: "Fredoka", "Arial Rounded MT Bold", sans-serif; font-weight: 600; color: var(--ink); line-height: 1; }
  .card--front .brand { left: 296px; top: 256px; }
  .card--front .brand__name { font-size: 44px; }

  /* back */
  .card--back .brand { left: 170px; top: 90px; }
  .card--back .brand__mark { width: 66px; height: 66px; }
  .card--back .brand__name { font-size: 54px; }
  .status { position: absolute; right: 172px; top: 168px; font-family: "Fredoka", "Arial Rounded MT Bold", sans-serif; font-weight: 600; font-size: 20px; color: var(--green); }
  .services { position: absolute; left: 0; right: 0; top: 268px; text-align: center; font-size: 18px; color: var(--ink); letter-spacing: -.2px; }
  .services span.sep { margin: 0 14px; }
</style>
</head>
<body>

<section class="card card--front" aria-label="Card front">
  <div class="holder">
    <div class="holder__name">Mark Pellow</div>
    <div class="holder__role">owner</div>
    <div class="holder__rule"></div>
  </div>

  <ul class="contacts">
    <li>
      <svg viewBox="0 0 16 16"><rect x="4" y="1" width="8" height="14" rx="1.5" fill="none" stroke="#8dc63f" stroke-width="1.6"/><circle cx="8" cy="12.5" r="0.9" fill="#8dc63f"/></svg>
      027 846 2093
    </li>
    <li>
      <svg viewBox="0 0 16 16"><rect x="1" y="3" width="14" height="10" fill="#8dc63f"/><path d="M1 3 L8 9 L15 3" fill="none" stroke="#fff" stroke-width="1.3"/></svg>
      markpellow@stockharbor.example
    </li>
    <li>
      <svg viewBox="0 0 16 16" fill="none" stroke="#8dc63f" stroke-width="1.2"><circle cx="8" cy="8" r="6.5"/><ellipse cx="8" cy="8" rx="3" ry="6.5"/><path d="M1.5 8 H14.5 M2.5 4.8 H13.5 M2.5 11.2 H13.5"/></svg>
      www.stockharbor.example
    </li>
  </ul>

  <div class="band band--dark"></div>
  <div class="band band--green"></div>

  <div class="brand">
    <span class="brand__mark"></span>
    <span class="brand__name">StockHarbor</span>
  </div>
</section>

<section class="card card--back" aria-label="Card back">
  <div class="brand">
    <span class="brand__mark"></span>
    <span class="brand__name">StockHarbor</span>
  </div>
  <div class="status">Coming soon</div>
  <p class="services">Sell Excess Stock<span class="sep">|</span>Manage Product Returns<span class="sep">|</span>Sell Company Assets</p>
</section>

</body>
</html>
```